PPE EQIUPMENT

WE WOULD LIKE TO PRODUCE 2 DIFFERENT BANNERS TO BE PLACED OUTSIDE OF OUR WAREHOUSE TO ADVERTISE THAT WE HAVE FACE MASKS, HAND SANITISERS, DISINFECTANT SPRAY, FACE SHIELDS AND HAND SOAP. THE SIZE OF EACH BANNER WILL BE , portrait to be (W) 140 cm x (H) 250 cm, with 4 x eyelets. THE BANNER IS TO STATE PPE EQUIPMENT AVAILABLE HERE AND SHOW OUR PHONE NUMBER 0207-946-0318. FINALLY WE WILL REQUIRE SOME IMAGES OF THE PRODUCTS IF YOU CAN SUPPLY THESE. THANKS

```html
<!DOCTYPE html>
<html lang="en">
<head>
<meta charset="utf-8">
<title>PPE Equipment Banner</title>
<link href="https://fonts.googleapis.com/css2?family=Anton&family=Arimo:wght@400&family=Bebas+Neue&family=Barlow:wght@300&family=Barlow+Semi+Condensed:wght@500&family=Russo+One&display=swap" rel="stylesheet">
<style>
  :root {
    --navy: #203a6f;
    --white: #ffffff;
    --backdrop: #d6d6d6;
    --tile-tint: #e4e9f2;
  }
  html, body {
    margin: 0;
    padding: 0;
    width: 960px;
    height: 1200px;
    overflow: hidden;
    background: var(--backdrop);
  }
  .banner {
    position: absolute;
    left: 167px;
    top: 40px;
    width: 626px;
    height: 1120px;
    background: var(--navy);
    overflow: hidden;
  }
  .banner-header {
    position: absolute;
    left: 0; top: 0;
    width: 100%;
    height: 225px;
    background: var(--white);
  }
  .line {
    position: absolute;
    left: 0;
    width: 100%;
    margin: 0;
    text-align: center;
    line-height: 1;
    white-space: nowrap;
  }
  .headline {
    top: 54px;
    font-family: "Anton", sans-serif;
    font-size: 96px;
    letter-spacing: -1px;
    color: var(--navy);
    transform: scaleX(0.98);
  }
  .subline {
    top: 156px;
    font-family: "Arimo", Arial, sans-serif;
    font-size: 50px;
    color: var(--navy);
  }
  .phone {
    top: 248px;
    font-family: "Russo One", sans-serif;
    font-size: 66px;
    color: var(--white);
    letter-spacing: 1px;
  }
  .product-tile {
    position: absolute;
    width: 233px;
    height: 105px;
    border-radius: 9px;
    background: radial-gradient(ellipse at center, var(--tile-tint) 0%, var(--white) 70%);
  }
  .tile-mask      { left: 52px;  top: 340px; }
  .tile-sanitiser { left: 334px; top: 340px; }
  .tile-soap      { left: 52px;  top: 555px; height: 107px; }
  .tile-shield    { left: 336px; top: 555px; height: 107px; }
  .tile-spray     { left: 202px; top: 757px; height: 108px; }
  .product-label {
    position: absolute;
    font-family: "Bebas Neue", sans-serif;
    font-size: 63px;
    line-height: 1;
    color: var(--white);
    white-space: nowrap;
    margin: 0;
  }
  .label-row-1 { top: 466px; }
  .label-row-2 { top: 683px; }
  .label-mask      { left: 26px; }
  .label-sanitiser { left: 275px; }
  .label-soap      { left: 68px; }
  .label-shield    { left: 305px; }
  .label-spray     { top: 874px; left: 0; width: 100%; text-align: center; }
  .brand-name {
    top: 978px;
    font-family: "Barlow Semi Condensed", sans-serif;
    font-weight: 500;
    font-size: 56px;
    letter-spacing: 1.5px;
    color: var(--white);
  }
  .brand-tagline {
    top: 1042px;
    font-family: "Barlow", sans-serif;
    font-weight: 300;
    font-size: 32px;
    letter-spacing: 1.5px;
    color: var(--white);
  }
</style>
</head>
<body>
  <main class="banner">
    <header class="banner-header">
      <h1 class="line headline">PPE EQUIPMENT</h1>
      <p class="line subline">AVAILABLE HERE</p>
    </header>

    <p class="line phone">0207-946-0318</p>

    <div class="product-tile tile-mask" role="img" aria-label="Pictogram of a face mask"></div>
    <div class="product-tile tile-sanitiser" role="img" aria-label="Pictogram of hands under a hand sanitiser pump bottle"></div>
    <p class="product-label label-row-1 label-mask">FACE MASKS</p>
    <p class="product-label label-row-1 label-sanitiser">HAND SANITISERS</p>

    <div class="product-tile tile-soap" role="img" aria-label="Pictogram of a hand holding a bar of soap"></div>
    <div class="product-tile tile-shield" role="img" aria-label="Pictogram of a face shield"></div>
    <p class="product-label label-row-2 label-soap">HAND SOAP</p>
    <p class="product-label label-row-2 label-shield">FACE SHIELDS</p>

    <div class="product-tile tile-spray" role="img" aria-label="Pictogram of a disinfectant spray bottle"></div>
    <p class="product-label label-spray">DISINFECTANT SPRAY</p>

    <p class="line brand-name">KEYSTONE FURNITURE</p>
    <p class="line brand-tagline">TRADE FURNITURE SOLUTIONS</p>
  </main>
</body>
</html>
```